Business card design and logo needed

We have been operating as Ridgeline Posts for 30 years but never had a logo and feel there is a need for one, but have no idea for a design.
We specialise in all types of rural fencing including post and wire, post and rail, electric, chainmesh and to a lesser extent, also do industrial security fencing.
Updates

Sorry, but website is ridgelineposts.example

No .au on the end!
My apologies

Regards, Darren

Target Market(s)

Rural/acreage property owners, particularly horse people.

Industry/Entity Type

Industrial

Contact Information for Business Card

Ridgeline Posts Darren Kellett 0499 572106. Lewis Kellett 0499 613720
Email: ridgelineposts@mailhub.example
Website: www.ridgelineposts.example

Requirements
Must have
• Would like to highlight website address - use the business card to advertise the website or to push them to check it out.

```html
<!DOCTYPE html>
<html lang="en">
<head>
<meta charset="utf-8">
<title>Ridgeline Posts – Business Card</title>
<link rel="stylesheet" href="https://fonts.googleapis.com/css2?family=Arimo:wght@400;700&display=swap">
<style>
  :root {
    --bg-light: #f4f5f7;
    --bg-mid: #c9ccd2;
    --bg-dark: #9a9ea6;
    --map-tone: #b3b7be;
    --globe-light: #cdd6e3;
    --globe-mid: #6f83a3;
    --globe-dark: #1f2f4d;
    --brand-blue: #1b7fd4;
    --contact-ink: #111111;
    --glow-blue: #1f6fd0;
    --white: #ffffff;
  }
  * { margin: 0; padding: 0; box-sizing: border-box; }
  html, body { width: 1200px; height: 635px; overflow: hidden; }
  body { font-family: "Arimo", Arial, sans-serif; background: var(--bg-light); }

  .card {
    position: relative;
    width: 1200px;
    height: 635px;
    overflow: hidden;
    background: radial-gradient(ellipse at 60% 40%, var(--bg-light) 0%, var(--bg-mid) 55%, var(--bg-dark) 100%);
  }

  .world-map {
    position: absolute;
    left: 60px; top: 40px;
    width: 1100px; height: 460px;
    border-radius: 45%;
    background: radial-gradient(ellipse at center, var(--map-tone) 0%, rgba(179,183,190,0.35) 55%, rgba(179,183,190,0) 75%);
    opacity: 0.7;
  }

  .sweep-lines { position: absolute; inset: 0; }

  .globe {
    position: absolute;
    left: 40px; top: 378px;
    width: 500px; height: 500px;
    border-radius: 50%;
    background: radial-gradient(circle at 40% 30%, var(--globe-light) 0%, var(--globe-mid) 45%, var(--globe-dark) 100%);
    box-shadow: 0 0 40px rgba(255,255,255,0.6);
  }

  .contacts {
    position: absolute;
    right: 12px; top: 16px;
    text-align: right;
    color: var(--contact-ink);
    font-weight: 700;
    font-size: 27px;
    line-height: 44px;
    text-shadow: 0 0 6px var(--white), 0 0 10px var(--white);
  }

  .brand-name {
    position: absolute;
    left: 88px; top: 196px;
    color: var(--brand-blue);
    font-weight: 700;
    font-size: 78px;
    letter-spacing: 1px;
    white-space: nowrap;
    text-shadow: 0 0 14px var(--white), 0 0 26px var(--white), 0 0 40px var(--white);
  }

  .brand-tagline {
    position: absolute;
    left: 508px; top: 300px;
    color: var(--brand-blue);
    font-weight: 700;
    font-size: 54px;
    letter-spacing: 1px;
    white-space: nowrap;
    text-shadow: 0 0 12px var(--white), 0 0 24px var(--white);
  }

  .web-contact {
    position: absolute;
    right: 12px; top: 512px;
    text-align: right;
    color: var(--white);
    font-weight: 700;
    font-size: 28px;
    line-height: 56px;
    white-space: nowrap;
    text-shadow: 0 0 6px var(--glow-blue), 0 0 12px var(--glow-blue), 0 0 18px var(--glow-blue);
  }
</style>
</head>
<body>
  <main class="card">
    <div class="world-map" role="img" aria-label="Faint grey world map spread across the background"></div>

    <svg class="sweep-lines" width="1200" height="635" viewBox="0 0 1200 635" aria-hidden="true">
      <path d="M1200 230 C 1050 330, 950 470, 900 635" fill="none" stroke="#ffffff" stroke-opacity="0.7" stroke-width="2"/>
      <path d="M1200 270 C 1070 360, 990 490, 950 635" fill="none" stroke="#ffffff" stroke-opacity="0.5" stroke-width="1.5"/>
      <path d="M1200 320 C 1090 400, 1030 510, 1005 635" fill="none" stroke="#ffffff" stroke-opacity="0.4" stroke-width="1"/>
      <path d="M0 420 C 300 380, 700 560, 1200 500" fill="none" stroke="#ffffff" stroke-opacity="0.35" stroke-width="1.5"/>
    </svg>

    <div class="globe" role="img" aria-label="Blue earth globe showing the Americas, rising from the lower left corner"></div>

    <div class="contacts">
      <p>Darren Kellett : 0499 572106</p>
      <p>Lewis Kellett : 0499 613720</p>
    </div>

    <h1 class="brand-name">Ridgeline Posts</h1>
    <p class="brand-tagline">&amp; metal fabrication</p>

    <div class="web-contact">
      <p>Website : www.ridgelineposts.example</p>
      <p>Email : ridgelineposts@mailhub.example</p>
    </div>
  </main>
</body>
</html>
```